KFL Noblesville Sign

I need to have a sign designed for a new self-storage facility we are going to be opening. The sign will be 4'W X 8'H.

Industry/Entity Type

Self Storage

Requirements
Must have
• Keystone Locker Hub logo at the top of the sign, under the logo I want the rendering.
• I also must have this information on the sign:
• 1. OPENING FALL 2016
• 2. Your premier self-storage facility.
• 3. www.keystonelockerhub.com

```html
<!DOCTYPE html>
<html lang="en">
<head>
<meta charset="utf-8">
<title>Keystone Locker Hub – Opening Fall 2016 Sign</title>
<link rel="stylesheet" href="https://fonts.googleapis.com/css2?family=Anton&family=Open+Sans:wght@700&family=Roboto+Condensed:wght@700&display=swap">
<style>
  :root {
    --sky-top: #2f7fd0;
    --sky-mid: #5aa7e4;
    --sky-low: #a9d6f2;
    --brand-yellow: #f8ec12;
    --brand-red: #e8202a;
    --ink: #111111;
    --white: #ffffff;
    --facade-light: #d6bf97;
    --facade-dark: #b39a72;
    --lawn: #7d9a3c;
    --lawn-edge: #2e9a3a;
  }
  * { margin: 0; padding: 0; box-sizing: border-box; }
  html, body {
    width: 686px;
    height: 1200px;
    overflow: hidden;
    background: var(--white);
  }
  .sign {
    position: relative;
    width: 686px;
    height: 1200px;
    overflow: hidden;
    background: linear-gradient(180deg, var(--sky-top) 0%, var(--sky-mid) 45%, var(--sky-low) 78%);
  }
  .brand-name {
    position: absolute;
    top: 78px;
    left: 0;
    width: 100%;
    text-align: center;
    font-family: "Roboto Condensed", "Arial Narrow", sans-serif;
    font-weight: 700;
    font-size: 96px;
    line-height: 112px;
    color: var(--brand-yellow);
  }
  .headline {
    position: absolute;
    top: 470px;
    left: 0;
    width: 686px;
    height: 240px;
  }
  .headline text { font-family: "Anton", Impact, sans-serif; }
  .headline .opening { fill: var(--brand-red); }
  .headline .year { fill: var(--brand-yellow); }
  .headline .shadow { fill: var(--ink); }
  .tagline {
    position: absolute;
    top: 722px;
    left: 0;
    width: 100%;
    text-align: center;
    font-family: "Open Sans", Verdana, sans-serif;
    font-weight: 700;
    font-size: 37px;
    line-height: 1.22;
    color: var(--ink);
  }
  .rendering {
    position: absolute;
    left: 0;
    top: 818px;
    width: 686px;
    height: 303px;
    background: linear-gradient(180deg, rgba(214,191,151,0) 0%, var(--facade-light) 24%, var(--facade-dark) 84%, var(--lawn) 93%, var(--lawn) 100%);
  }
  .lawn-edge {
    position: absolute;
    left: 0;
    top: 1121px;
    width: 686px;
    height: 4px;
    background: var(--lawn-edge);
  }
  .web-band {
    position: absolute;
    left: 0;
    top: 1125px;
    width: 686px;
    height: 75px;
    background: var(--brand-red);
    display: flex;
    align-items: center;
    justify-content: center;
    font-family: "Roboto Condensed", "Arial Narrow", sans-serif;
    font-weight: 700;
    font-size: 38px;
    color: var(--white);
  }
  .web-band .accent { color: var(--brand-yellow); }
</style>
</head>
<body>
  <main class="sign">
    <h1 class="brand-name">Keystone<br>Locker<br>Hub</h1>

    <svg class="headline" viewBox="0 0 686 240" aria-label="Opening Fall 2016">
      <text class="shadow" x="79" y="76" font-size="80" textLength="536" lengthAdjust="spacingAndGlyphs">OPENING FALL</text>
      <text class="opening" x="75" y="72" font-size="80" textLength="536" lengthAdjust="spacingAndGlyphs">OPENING FALL</text>
      <text class="shadow" x="134" y="234" font-size="176" textLength="428" lengthAdjust="spacingAndGlyphs">2016</text>
      <text class="year" x="129" y="230" font-size="176" textLength="428" lengthAdjust="spacingAndGlyphs">2016</text>
    </svg>

    <p class="tagline">Your Premier<br>Self-storage Facility.</p>

    <div class="rendering" role="img" aria-label="Architectural rendering of the new three-storey self-storage building with tan facade, stone pilasters, green roll-up doors and lawn in front"></div>
    <div class="lawn-edge"></div>

    <footer class="web-band">
      <span class="accent">www.</span>KeystoneLockerHub<span class="accent">.com</span>
    </footer>
  </main>
</body>
</html>
```